Private lender of mortgages and rent to own housing

need a website that reflects real estate especially mortgage lending and rent to own houses..
Sections as follows
Home About Types of mortgages Rent to own Contact us
Target Market(s)
consumers who require non traditonal mortgages
Industry/Entity Type
Mortgage
Coding
Coded - Design and coding required
Number of Pages Required
4 page
Font styles to use
Sans Serif
Colors
Designer to choose colors to be used in the design.
Requirements
Must have
- background pictures on pages. with nice picture on homepage of houses or a community
Nice to have
- contact us form i supplied a ink to

```html
<!DOCTYPE html>
<html lang="en">
<head>
<meta charset="utf-8">
<title>Harbourline Lending Group — Rent to Own a Home</title>
<link rel="stylesheet" href="https://fonts.googleapis.com/css2?family=Raleway:wght@400;600;700;800&family=Open+Sans:wght@400;600;700&display=swap">
<style>
:root{
  --navy:#2d2b6e;
  --navy-deep:#26245c;
  --orange:#f08a24;
  --orange-dark:#e07a14;
  --text:#555a66;
  --light:#e4e9f0;
  --white:#ffffff;
}
*{box-sizing:border-box;margin:0;padding:0}
html,body{width:1200px;height:4353px;overflow:hidden}
body{font-family:"Open Sans",Arial,sans-serif;color:var(--text);background:var(--white);font-size:14px;line-height:1.75}
h1,h2,h3,h4{font-family:"Raleway",Arial,sans-serif}
section,header,footer{position:relative;width:1200px;overflow:hidden}

/* hero */
.hero{height:625px}
.hero-photo{position:absolute;inset:0;background:
  radial-gradient(ellipse at 55% 80%,rgba(240,170,80,.55),transparent 45%),
  linear-gradient(180deg,#c9d6df 0%,#6f7f7a 25%,#3c4a3f 55%,#2a2f28 80%,#1f2420 100%)}
.site-header{position:absolute;top:0;left:0;width:1200px;height:116px;background:linear-gradient(180deg,rgba(255,255,255,.97) 0%,rgba(255,255,255,.9) 80%,rgba(255,255,255,0) 100%);z-index:2}
.brand{position:absolute;left:34px;top:22px;display:flex;flex-direction:column;align-items:center;gap:8px}
.brand-mark{width:44px;height:44px;border-radius:50%;background:var(--navy)}
.brand-name{font-family:"Raleway",sans-serif;font-weight:700;font-size:16px;color:var(--navy);letter-spacing:.3px}
.main-nav{position:absolute;right:210px;top:28px;display:flex;gap:24px;font-family:"Raleway",sans-serif;font-weight:700;font-size:13px;color:var(--navy)}
.main-nav .active{color:var(--orange)}
.header-phone{position:absolute;right:34px;top:22px;background:var(--orange);color:#fff;font-weight:700;font-size:15px;padding:4px 14px;border-radius:3px;display:flex;align-items:center;gap:6px}
.hero-content{position:absolute;top:280px;left:0;width:1200px;text-align:center;color:#fff;z-index:1}
.hero-content h1{font-size:50px;font-weight:800;letter-spacing:.5px;line-height:1.1}
.hero-content p{font-size:22px;margin-top:8px}
.btn{display:inline-flex;align-items:center;gap:10px;font-family:"Raleway",sans-serif;font-weight:700;font-size:15px;color:#fff;border-radius:24px;padding:10px 28px}
.btn-orange{background:var(--orange)}
.btn-navy{background:var(--navy)}
.hero-content .btn{margin-top:22px}
.hero-dots{position:absolute;bottom:12px;left:50%;transform:translateX(-50%);display:flex;gap:8px;background:rgba(255,255,255,.9);padding:6px 12px}
.hero-dots span{width:8px;height:8px;border-radius:50%;background:#9aa3b5}
.hero-dots span:first-child{background:var(--navy)}

.section-title{text-align:center;font-weight:800;text-transform:uppercase;color:var(--navy);font-size:30px}
.section-title::after{content:"";display:block;width:56px;height:4px;background:var(--orange);margin:10px auto 0}

/* welcome */
.welcome{height:378px;padding-top:52px}
.welcome .cols{display:flex;gap:40px;padding:0 150px;margin-top:38px}
.welcome p{flex:1;font-size:13.5px;line-height:2.05}
.welcome p:first-child{text-align:center}

/* application */
.application{height:668px;background:var(--orange);padding-top:66px;color:#fff}
.application .section-title{color:#fff;font-size:32px}
.application .section-title::after{background:var(--navy)}
.application .cols{display:flex;gap:46px;padding:0 170px;margin-top:46px}
.application .col{flex:1;font-size:15px;line-height:1.75}
.application .col p{margin-bottom:28px}
.application .btn{margin-top:10px}

/* features */
.features{height:770px;padding:131px 130px 0}
.feature-grid{display:grid;grid-template-columns:repeat(4,1fr);gap:24px}
.feature{position:relative}
.feature.highlight{background:var(--orange);margin:-10px -12px 0;padding:10px 12px 30px;color:#fff}
.feature-photo{height:160px;position:relative}
.feature-photo .go{position:absolute;right:6px;bottom:-10px;width:28px;height:28px;border-radius:50%;background:var(--orange);display:flex;align-items:center;justify-content:center}
.feature.highlight .feature-photo .go{background:var(--navy)}
.feature h3{font-size:17px;font-weight:800;color:var(--navy);text-transform:uppercase;margin-top:20px}
.feature.highlight h3{color:#fff}
.feature p{font-size:13.5px;line-height:1.85;margin-top:10px}

/* testimonials */
.testimonials{height:581px}
.testimonials-photo{position:absolute;inset:0;background:linear-gradient(180deg,rgba(45,43,110,.82),rgba(45,43,110,.78)),linear-gradient(90deg,#7d8b95,#a7b2b7 50%,#6e7c83)}
.testimonials h2{position:relative;color:#fff;text-align:center;font-size:34px;font-weight:800;padding-top:50px}
.quote-mark{position:relative;text-align:center;color:#fff;font-family:Georgia,serif;font-size:60px;font-weight:700;line-height:.6;margin-top:14px}
.testimonial-row{position:relative;display:flex;gap:30px;padding:0 130px;margin-top:22px}
.testimonial{flex:1;background:#fff;height:335px;text-align:center;padding:30px 34px 0;position:relative}
.testimonial blockquote{font-family:Georgia,"Times New Roman",serif;font-style:italic;font-size:15px;color:#333;line-height:1.6}
.stars{color:var(--orange);font-size:18px;letter-spacing:3px;margin-top:18px}
.testimonial cite{display:block;font-style:normal;font-weight:700;color:var(--navy);font-size:14px}
.testimonial .role{font-size:13px}
.avatar{position:absolute;left:50%;bottom:-72px;transform:translateX(-50%);width:110px;height:110px;border-radius:50%;border:5px solid #fff;background:linear-gradient(135deg,#c9ccd3,#8d939e)}
.slide-arrow{position:absolute;top:290px}
.slide-arrow.prev{left:20px}.slide-arrow.next{right:20px}

/* faq */
.faq{height:581px;padding-top:70px}
.faq .sub{text-align:center;font-family:"Raleway",sans-serif;font-weight:700;color:var(--navy);font-size:19px;margin-top:22px}
.faq-grid{display:grid;grid-template-columns:1fr 1fr;column-gap:45px;row-gap:24px;padding:0 125px;margin-top:42px}
.faq-item{height:46px;border-radius:23px;background:var(--navy);color:#fff;display:flex;align-items:center;justify-content:center;gap:16px;font-size:16px}
.faq-item .plus{width:20px;height:20px;border-radius:50%;background:#fff;color:var(--navy);font-weight:700;font-size:14px;display:flex;align-items:center;justify-content:center;line-height:1}
.faq .more{text-align:center;margin-top:44px}

/* newsletter */
.newsletter{height:146px;background:var(--light);display:flex;align-items:center;padding-left:270px;gap:50px}
.newsletter h4{font-weight:700;color:var(--navy);font-size:17px;line-height:1.35;width:210px}
.newsletter form{display:flex}
.newsletter .field{width:390px;height:48px;background:#fff;border:0;padding:0 18px;color:#9aa0aa;font-size:16px;display:flex;align-items:center}
.newsletter .submit{width:230px;height:48px;background:var(--navy);color:#fff;font-family:"Raleway",sans-serif;font-weight:800;font-size:16px;display:flex;align-items:center;justify-content:center;margin-left:12px}

/* footer */
.site-footer{height:551px;background:var(--navy);color:#fff;padding:46px 130px 0;display:flex}
.footer-about{width:320px}
.footer-about .brand-mark{background:#fff;margin-left:62px}
.footer-about .brand-name{color:#fff;display:block;margin-top:12px;font-size:17px}
.contact-list{list-style:none;margin-top:22px;font-size:14px}
.contact-list li{display:flex;gap:12px;margin-bottom:16px;align-items:flex-start}
.contact-list li.phone{font-size:24px;align-items:center}
.social{display:flex;gap:24px;margin-top:28px}
.social span{width:24px;height:24px;border-radius:50%;background:#fff;opacity:.9}
.footer-links{width:210px}
.footer-links h4{font-size:19px;font-weight:700;margin-top:58px}
.footer-links ul{list-style:none;font-size:14px;margin-top:4px;line-height:2.05;color:#d9dbef}
.contact-form{flex:1;display:grid;grid-template-columns:1fr 1fr;gap:12px 14px;align-content:start;padding-top:50px}
.contact-form .input{height:38px;border:1px solid #fff;background:rgba(255,255,255,.95);color:#555;font-size:14px;padding:6px 10px}
.contact-form .message{grid-column:1/3;height:150px}
.contact-form .submit{grid-column:1/2;width:165px;height:40px;border-radius:20px;background:var(--orange);color:#fff;font-family:"Raleway",sans-serif;font-weight:800;letter-spacing:1px;display:flex;align-items:center;justify-content:center;margin-top:30px}
.copyright{height:53px;background:var(--navy-deep);color:#cfd1e6;text-align:center;font-size:13px;line-height:53px}
</style>
</head>
<body>

<section class="hero">
  <div class="hero-photo" role="img" aria-label="Large family home lit warmly at dusk, surrounded by trees"></div>
  <header class="site-header">
    <div class="brand"><span class="brand-mark"></span><span class="brand-name">HARBOURLINE LENDING GROUP</span></div>
    <nav class="main-nav"><span class="active">HOME</span><span>ABOUT</span><span>TYPES OF MORTGAGES</span><span>RENT TO OWN</span><span>CONTACT US</span></nav>
    <div class="header-phone">
      <svg width="14" height="14" viewBox="0 0 24 24"><path fill="#fff" d="M6.6 10.8a15 15 0 0 0 6.6 6.6l2.2-2.2c.3-.3.7-.4 1-.2 1.1.4 2.3.6 3.6.6.6 0 1 .4 1 1V20c0 .6-.4 1-1 1A17 17 0 0 1 3 4c0-.6.4-1 1-1h3.5c.6 0 1 .4 1 1 0 1.3.2 2.5.6 3.6.1.3 0 .7-.2 1z"/></svg>1.800.555.0199
    </div>
  </header>
  <div class="hero-content">
    <h1>RENT TO OWN A HOME</h1>
    <p>We can put you in your own home today!</p>
    <span class="btn btn-orange">APPLY NOW <span>›</span></span>
  </div>
  <div class="hero-dots"><span></span><span></span><span></span></div>
</section>

<section class="welcome">
  <h2 class="section-title">Welcome</h2>
  <div class="cols">
    <p>We know life sometimes delivers challenges and it can be hard to get back on track once you have dealt with challenges. Maybe you have been through a divorce, bankruptcy, consumer proposal, loss of job, work place injury, new to the country, self-employed or some credit related challenges that have you behind the eight ball? Are these challenges making it difficult to get a</p>
    <p>mortgage? None of these things has to bind you to a lifetime of renting. Want to start paying yourself first? We focus on rent to own in Simcoe County and our Renting Program is a very viable option for those that can't get a mortgage today but are willing to work towards getting approved in the near future while living in their own home that they select. Homeownership is closer than you think.</p>
  </div>
</section>

<section class="application">
  <h2 class="section-title">Rent-to-Own A Home Program Application</h2>
  <div class="cols">
    <div class="col">
      <p>Thank you for applying for our Ontario Rent-to-Own A Home Program. For each applicant, please complete and submit a separate application.</p>
      <p>This preliminary application is the first step in our Rent-To-Own A Home Program. For an overview of all the steps involved, please visit our section on How our Rent-To-Own Program Works.</p>
      <p>To qualify and to ensure success in the program you must be genuinely motivated and committed to improving your current situation. You must also be able to cover your old debts plus your new lease</p>
    </div>
    <div class="col">
      <p>payments. To learn more about what you need to qualify, read our Tenant Buyers Qualification Section.</p>
      <p>All information submitted to us will remain strictly confidential and will not be shared. There is no obligation assumed by submitting this application. This application will only be used to pre-qualify you for our Rent-To-Own A Home Program. Once submitted, we will contact you within 24 hours to confirm the details you provided and to discuss your current credit situation in more detail.</p>
      <span class="btn btn-navy">APPLY NOW <span>›</span></span>
    </div>
  </div>
</section>

<section class="features">
  <div class="feature-grid">
    <article class="feature">
      <div class="feature-photo" role="img" aria-label="Suburban house with front lawn" style="background:linear-gradient(160deg,#9fb6c9,#7d8a6a 60%,#5e6b4a)"><span class="go"><svg width="12" height="12" viewBox="0 0 12 12"><path d="M4 2l4 4-4 4" stroke="#fff" stroke-width="2" fill="none"/></svg></span></div>
      <h3>Down Payment</h3>
      <p>We require a minimum down payment of $10,000 or 2.5% to 4% of the total price of the home (whichever is larger). So a $400,000 will require a bigger down than a $300,000 house. This is 100% credited towards your purchase of the home. Your down payment is required at the time we have the home inspection.</p>
    </article>
    <article class="feature highlight">
      <div class="feature-photo" role="img" aria-label="Family home with garden" style="background:linear-gradient(160deg,#b7c7d3,#9c8f7a 55%,#6b7a55)"><span class="go"><svg width="12" height="12" viewBox="0 0 12 12"><path d="M4 2l4 4-4 4" stroke="#fff" stroke-width="2" fill="none"/></svg></span></div>
      <h3>Household Income</h3>
      <p>Steady, provable household income that can support the price of the home you would like. A general guideline is minimum of $50,000 annually but this depends on the price of home you wish to purchase.</p>
    </article>
    <article class="feature">
      <div class="feature-photo" role="img" aria-label="Modern two-storey home in daylight" style="background:linear-gradient(160deg,#c7d4df,#a9aba3 55%,#6f7a6a)"><span class="go"><svg width="12" height="12" viewBox="0 0 12 12"><path d="M4 2l4 4-4 4" stroke="#fff" stroke-width="2" fill="none"/></svg></span></div>
      <h3>Credit Report</h3>
      <p>Although your credit won't necessarily disqualify you from our rent to own program, it is important to know where you stand and what will be needed to improve it while you are in the program. We provide support, you provide the "doing". Credit repair is a commitment.</p>
    </article>
    <article class="feature">
      <div class="feature-photo" role="img" aria-label="Contemporary house with large windows" style="background:linear-gradient(160deg,#a6c0d6,#8a9aa4 55%,#5b6a60)"><span class="go"><svg width="12" height="12" viewBox="0 0 12 12"><path d="M4 2l4 4-4 4" stroke="#fff" stroke-width="2" fill="none"/></svg></span></div>
      <h3>Selecting a House</h3>
      <p>May not seem like a strong determining factor overall for qualifying for rent to own but it is for us. You should WANT to select your house as this might be the biggest determining success factor. With our program, you should commit the time to working with one of our realtors to find the "right" house. If you don't love the house, it is going to make it harder to succeed.</p>
    </article>
  </div>
</section>

<section class="testimonials">
  <div class="testimonials-photo" role="img" aria-label="Row of suburban houses under a blue tint"></div>
  <h2>What our clients say</h2>
  <div class="quote-mark">"</div>
  <svg class="slide-arrow prev" width="24" height="44" viewBox="0 0 24 44"><path d="M20 2L4 22l16 20" stroke="#fff" stroke-width="2" fill="none"/></svg>
  <svg class="slide-arrow next" width="24" height="44" viewBox="0 0 24 44"><path d="M4 2l16 20L4 42" stroke="#fff" stroke-width="2" fill="none"/></svg>
  <div class="testimonial-row">
    <figure class="testimonial">
      <blockquote>Lorem ipsum dolor sit amet, consectetur adipiscing elit. Ut malesuada urna non lacus tempus accumsan. Aenean eget condimentum elit. Pellentesque a orci in lacus rhoncus.</blockquote>
      <div class="stars">★★★★★</div>
      <cite>Mr. Daniel Reeves</cite><div class="role">Satisfied client</div>
      <div class="avatar" role="img" aria-label="Client portrait"></div>
    </figure>
    <figure class="testimonial">
      <blockquote>Lorem ipsum dolor sit amet, consectetur adipiscing elit. Ut malesuada urna non lacus tempus accumsan. Aenean eget condimentum elit. Pellentesque a orci in lacus rhoncus.</blockquote>
      <div class="stars">★★★★★</div>
      <cite>Mrs Helena Marsh</cite><div class="role">Satisfied client</div>
      <div class="avatar" role="img" aria-label="Client portrait"></div>
    </figure>
    <figure class="testimonial">
      <blockquote>Lorem ipsum dolor sit amet, consectetur adipiscing elit. Ut malesuada urna non lacus tempus accumsan. Aenean eget condimentum elit. Pellentesque a orci in lacus rhoncus.</blockquote>
      <div class="stars">★★★★★</div>
      <cite>Mr. Alan Whitby</cite><div class="role">Satisfied client</div>
      <div class="avatar" role="img" aria-label="Client portrait"></div>
    </figure>
  </div>
</section>

<section class="faq">
  <h2 class="section-title">Rent-to-Own A Home</h2>
  <p class="sub">Frequently Asked Questions</p>
  <div class="faq-grid">
    <div class="faq-item">What is Rent-To-Own A Home? <span class="plus">+</span></div>
    <div class="faq-item">How does your Rent-To-Own A Home Program work? <span class="plus">+</span></div>
    <div class="faq-item">Who is Rent-To-Own A Home suited for? <span class="plus">+</span></div>
    <div class="faq-item">Do I get to choose my own home? <span class="plus">+</span></div>
    <div class="faq-item">Can I choose any city in Ontario to live in? <span class="plus">+</span></div>
    <div class="faq-item">Who will be paying the utility bills? <span class="plus">+</span></div>
  </div>
  <div class="more"><span class="btn btn-orange">READ ALL FAQ <span>›</span></span></div>
</section>

<section class="newsletter">
  <h4>Subscribe to our newsletter and receive latest update.</h4>
  <form>
    <div class="field">Your email</div>
    <div class="submit">SUBSCRIBE</div>
  </form>
</section>

<footer class="site-footer">
  <div class="footer-about">
    <span class="brand-mark" style="display:block"></span>
    <span class="brand-name">HARBOURLINE LENDING GROUP</span>
    <ul class="contact-list">
      <li><svg width="18" height="22" viewBox="0 0 18 22"><path d="M9 1a7 7 0 0 0-7 7c0 5 7 13 7 13s7-8 7-13a7 7 0 0 0-7-7z" stroke="#fff" stroke-width="1.6" fill="none"/><circle cx="9" cy="8" r="2.5" fill="#fff"/></svg><span>120 Maple Court, Barrie<br>L4M 3B1, Ontario, Canada</span></li>
      <li class="phone"><svg width="20" height="20" viewBox="0 0 24 24"><path fill="none" stroke="#fff" stroke-width="1.6" d="M6.6 10.8a15 15 0 0 0 6.6 6.6l2.2-2.2c.3-.3.7-.4 1-.2 1.1.4 2.3.6 3.6.6.6 0 1 .4 1 1V20c0 .6-.4 1-1 1A17 17 0 0 1 3 4c0-.6.4-1 1-1h3.5c.6 0 1 .4 1 1 0 1.3.2 2.5.6 3.6.1.3 0 .7-.2 1z"/></svg>1.800.555.0199</li>
      <li><svg width="20" height="16" viewBox="0 0 20 16"><rect x="1" y="1" width="18" height="14" stroke="#fff" stroke-width="1.6" fill="none"/><path d="M1 1l9 8 9-8" stroke="#fff" stroke-width="1.6" fill="none"/></svg>info@harbourlinelending.ca</li>
    </ul>
    <div class="social"><span></span><span></span><span></span><span></span></div>
  </div>
  <div class="footer-links">
    <h4>Quick Links</h4>
    <ul><li>Home</li><li>About</li><li>Types of Mortgages</li><li>Rent To Own</li><li>FAQ</li><li>Program Application</li><li>Contact Us</li></ul>
  </div>
  <form class="contact-form">
    <div class="input">Name</div>
    <div class="input">Email</div>
    <div class="input">Phone No</div>
    <div class="input">Subject</div>
    <div class="input message">Message</div>
    <div class="submit">SUBMIT</div>
  </form>
</footer>
<div class="copyright">© Copyright 2017. Harbourline Lending Group. All rights reserved.</div>

</body>
</html>
```